Quiet Harbor Counseling Business Card design with a visually interesting use of Space

I need business cards that are luxurious and give a peaceful, calm vibe. I also had some letterhead designed, and i like the look of it also, it's attached with the logo design for reference/ ideas but feel free to be creative.

Target Market(s)

High end luxurious client who needs counseling

Industry/Entity Type

Marriage and Family Therapy

Contact Information for Business Card

Corra Mabbitt MS LMFT/ or Tobin Walsh address 4175 Pemberly Suite 620

Font styles to use
Sans Serif

Colors
0054AA
0677BA
7BADD7
CADEEF
E8F1F8
0094D4
00A9DD
6FCCEA
C7EBF8
E9F6FB
A7469A
B969AE
D3A5CF
EDDBEB
F8F0F9
6B429C
8869AF
B7A5CE
E3DAEB
F3F0F8

Requirements
Must have
• Logo and color scheme but be simple modern and luxurious
Nice to have
• I'd like to incorporate some elelmets from the logo and letterhead into a simple modern card

```html
<!DOCTYPE html>
<html lang="en">
<head>
<meta charset="utf-8">
<title>Quiet Harbor Counseling — Business Card</title>
<link rel="stylesheet" href="https://fonts.googleapis.com/css2?family=Quicksand:wght@300;400&family=Nunito+Sans:wght@300;400&display=swap">
<style>
  :root {
    --stage: #e9e6e3;
    --paper: #ffffff;
    --paper-shade: #f1f1f1;
    --night: #141617;
    --night-deep: #050505;
    --ink: #2a2a2a;
    --ink-soft: #6a6a6a;
    --ink-light: #f2f2f2;
    --teal: #3fa9a5;
    --pink: #d3a5cf;
    --plum: #a7469a;
    --violet: #6b429c;
    --blue: #0677ba;
  }
  * { box-sizing: border-box; margin: 0; padding: 0; }
  html, body {
    width: 1200px; height: 960px; overflow: hidden;
    background: var(--stage);
    font-family: "Nunito Sans", sans-serif;
  }
  .stage { position: relative; width: 1200px; height: 960px; }
  .card {
    position: absolute; left: 220px; width: 760px; height: 434px;
    overflow: hidden;
    box-shadow: 0 6px 18px rgba(0,0,0,0.18);
  }
  .card--front {
    top: 24px;
    background: linear-gradient(135deg, var(--paper) 35%, var(--paper-shade) 100%);
  }
  .card--back {
    top: 502px;
    background: linear-gradient(135deg, var(--night) 0%, var(--night-deep) 100%);
  }
  .tone-field { position: absolute; left: 0; top: 0; width: 760px; height: 434px; }

  .wordmark {
    position: absolute; z-index: 1;
    display: flex; align-items: center; gap: 14px;
  }
  .wordmark__text {
    font-family: "Quicksand", sans-serif; font-weight: 300;
    display: flex; flex-direction: column; align-items: flex-end;
    line-height: 1;
  }
  .wordmark__name { font-size: 40px; letter-spacing: 0.5px; }
  .wordmark__sub { font-size: 17px; letter-spacing: 6px; margin-top: 4px; margin-right: -6px; }
  .wordmark__dot {
    width: 30px; height: 30px; border-radius: 50%;
    background: var(--violet); opacity: 0.75;
  }
  .card--front .wordmark { left: 250px; top: 52px; }
  .card--front .wordmark__text { color: var(--ink); }
  .card--back .wordmark { left: 120px; top: 160px; }
  .card--back .wordmark__text { color: var(--ink-light); }
  .card--back .wordmark__name { font-size: 46px; }
  .card--back .wordmark__sub { font-size: 19px; }

  .person { position: absolute; left: 72px; top: 142px; }
  .person__name {
    font-family: "Quicksand", sans-serif; font-weight: 400;
    font-size: 28px; color: var(--teal); letter-spacing: 0.5px;
  }
  .person__role {
    font-family: "Quicksand", sans-serif; font-weight: 400;
    font-size: 17px; color: var(--ink-soft); margin-top: 2px;
  }
  .divider {
    position: absolute; left: 72px; top: 226px;
    width: 44px; height: 2px; background: var(--pink);
  }
  .contacts { position: absolute; left: 72px; top: 250px; list-style: none; }
  .contacts__item {
    display: flex; align-items: center; gap: 12px;
    font-size: 17px; color: var(--ink-soft); height: 31px;
  }
  .contacts__icon { width: 18px; height: 18px; fill: var(--teal); flex: none; }
  .contacts__icon--line { fill: none; stroke: var(--teal); stroke-width: 1.8; }
</style>
</head>
<body>
<main class="stage">
  <section class="card card--front" aria-label="Business card front">
    <svg class="tone-field" viewBox="0 0 760 434" role="img" aria-label="Soft purple, plum and blue tone area for the decorative circles">
      <defs>
        <linearGradient id="front-tone" x1="0" y1="0" x2="1" y2="1">
          <stop offset="0" stop-color="#a7469a"/>
          <stop offset="0.5" stop-color="#6b429c"/>
          <stop offset="1" stop-color="#0677ba"/>
        </linearGradient>
      </defs>
      <circle cx="700" cy="370" r="215" fill="url(#front-tone)" opacity="0.85"/>
    </svg>

    <div class="wordmark">
      <div class="wordmark__text">
        <span class="wordmark__name">Quiet Harbor</span>
        <span class="wordmark__sub">Counseling</span>
      </div>
      <span class="wordmark__dot"></span>
    </div>

    <div class="person">
      <p class="person__name">Tobin Walsh</p>
      <p class="person__role">Consultant</p>
    </div>
    <div class="divider"></div>

    <ul class="contacts">
      <li class="contacts__item">
        <svg class="contacts__icon" viewBox="0 0 24 24" aria-hidden="true"><path d="M6.6 10.8a15.1 15.1 0 0 0 6.6 6.6l2.2-2.2a1 1 0 0 1 1-.25 11.4 11.4 0 0 0 3.6.57 1 1 0 0 1 1 1V20a1 1 0 0 1-1 1A17 17 0 0 1 3 4a1 1 0 0 1 1-1h3.5a1 1 0 0 1 1 1c0 1.25.2 2.45.57 3.57a1 1 0 0 1-.25 1z"/></svg>
        <span>369-555-0142</span>
      </li>
      <li class="contacts__item">
        <svg class="contacts__icon" viewBox="0 0 24 24" aria-hidden="true"><path d="M7 3h8l2 2v4H7z M4 10h16a1 1 0 0 1 1 1v7a1 1 0 0 1-1 1H4a1 1 0 0 1-1-1v-7a1 1 0 0 1 1-1z M7 15h10v6H7z"/></svg>
        <span>369-555-0187</span>
      </li>
      <li class="contacts__item">
        <svg class="contacts__icon contacts__icon--line" viewBox="0 0 24 24" aria-hidden="true"><path d="M3 5h18v14H3z M3 5l9 8 9-8"/></svg>
        <span>hello@quietharbor.com</span>
      </li>
      <li class="contacts__item">
        <svg class="contacts__icon contacts__icon--line" viewBox="0 0 24 24" aria-hidden="true"><circle cx="12" cy="12" r="9"/><ellipse cx="12" cy="12" rx="4" ry="9"/><path d="M3 12h18M5 7h14M5 17h14"/></svg>
        <span>www.quietharbor.com</span>
      </li>
    </ul>
  </section>

  <section class="card card--back" aria-label="Business card back">
    <svg class="tone-field" viewBox="0 0 760 434" role="img" aria-label="Soft purple, plum and blue tone area for the decorative circles">
      <defs>
        <linearGradient id="back-tone" x1="0" y1="0" x2="1" y2="1">
          <stop offset="0" stop-color="#a7469a"/>
          <stop offset="0.5" stop-color="#6b429c"/>
          <stop offset="1" stop-color="#0054aa"/>
        </linearGradient>
      </defs>
      <circle cx="720" cy="190" r="225" fill="url(#back-tone)" opacity="0.7"/>
    </svg>

    <div class="wordmark">
      <div class="wordmark__text">
        <span class="wordmark__name">Quiet Harbor</span>
        <span class="wordmark__sub">Counseling</span>
      </div>
    </div>
  </section>
</main>
</body>
</html>
```